Visitenkarten-Design für Psychiaterin
Zielgruppe
Dr. med. Monika Haberl, Ärztin, Psychotherapie für Kinder Jugendliche und Erwachsene, spezialisiert auf komplexe Posttraumatische Belastungsstörung, Dissoziative Störungen, Persönlichkeitsstörungen, Bindungsstörungen, LUMO-Mentorin
Das Design soll modern sein, Seriosität Professionalität, Dynamik und Geborgenheit ausstrahlen. Zielgruppe sind Menschen die traumatische Situationen überlebt haben.
Aufgabenstellung
Name, Fachgebiet und Spezialisierung, Telefonnummer, e-Mail
Unter Dateiupload sind Visitenkartenbeispiele die mir gefallen

```html
<!DOCTYPE html>
<html lang="de">
<head>
<meta charset="utf-8">
<title>Visitenkarte – Dr. med. Monika Haberl</title>
<link rel="stylesheet" href="https://fonts.googleapis.com/css2?family=Mulish:wght@400;600;700;800&display=swap">
<style>
  :root {
    --stage: #e6e7e8;
    --paper: #fbfcfc;
    --sage: #a6c79f;
    --sky-light: #adc6e6;
    --sky-deep: #8fabd8;
    --ink: #1c1c1e;
    --ink-soft: #2e2f33;
  }
  * { box-sizing: border-box; margin: 0; padding: 0; }
  html, body { width: 1200px; height: 800px; overflow: hidden; }
  body {
    background: var(--stage);
    font-family: "Mulish", "Avenir Next", sans-serif;
    color: var(--ink);
    position: relative;
  }
  .card {
    position: absolute;
    top: 225px;
    width: 540px;
    height: 350px;
    background: var(--paper);
    overflow: hidden;
    box-shadow: 0 6px 18px rgba(0,0,0,0.12);
  }
  .card--info { left: 40px; }
  .card--brand { left: 620px; }

  .card__backdrop { position: absolute; inset: 0; }

  .info {
    position: absolute;
    top: 20px;
    right: 22px;
    text-align: right;
  }
  .info__name {
    font-size: 22px;
    font-weight: 700;
    letter-spacing: 0.3px;
    margin-bottom: 8px;
  }
  .info__field,
  .info__focus li {
    font-size: 12.5px;
    font-weight: 400;
    line-height: 1.38;
    color: var(--ink-soft);
    letter-spacing: 0.3px;
  }
  .info__focus { list-style: none; margin-top: 18px; }
  .info__contact {
    position: absolute;
    right: 22px;
    bottom: 26px;
    text-align: right;
    font-size: 12.5px;
    font-weight: 700;
    line-height: 1.45;
  }

  .brand {
    position: absolute;
    left: 70px;
    top: 112px;
    display: flex;
    align-items: center;
    gap: 22px;
  }
  .brand__dot {
    width: 96px;
    height: 96px;
    border-radius: 50%;
    background: var(--sky-light);
    flex: none;
  }
  .brand__title {
    font-size: 38px;
    font-weight: 400;
    line-height: 1;
    letter-spacing: 0.2px;
  }
  .brand__tagline {
    font-size: 12.5px;
    font-weight: 400;
    margin-top: 6px;
    color: var(--ink-soft);
  }
  .brand__name {
    font-size: 20px;
    font-weight: 700;
    margin-top: 14px;
  }
</style>
</head>
<body>

  <section class="card card--info" aria-label="Rückseite der Visitenkarte">
    <svg class="card__backdrop" width="540" height="350" viewBox="0 0 540 350" aria-hidden="true">
      <defs>
        <linearGradient id="skyFade" x1="0" y1="0" x2="0.3" y2="1">
          <stop offset="0" stop-color="var(--sky-light)"/>
          <stop offset="1" stop-color="var(--sky-deep)"/>
        </linearGradient>
      </defs>
      <rect width="540" height="350" fill="var(--sage)"/>
      <circle cx="560" cy="300" r="500" fill="url(#skyFade)" stroke="var(--paper)" stroke-width="13"/>
    </svg>

    <div class="info">
      <h1 class="info__name">Dr. med. Monika Haberl</h1>
      <p class="info__field">Psychotherapie<br>für Kinder Jugendliche und Erwachsene</p>
      <ul class="info__focus">
        <li>komplexe Posttraumatische Belastungsstörung</li>
        <li>Dissoziative Störungen</li>
        <li>Persönlichkeitsstörungen</li>
        <li>Bindungsstörungen</li>
        <li>LUMO-Mentorin</li>
      </ul>
    </div>

    <p class="info__contact">Telefon 0761 4829 310<br>praxis@haberlmonika.de</p>
  </section>

  <section class="card card--brand" aria-label="Vorderseite der Visitenkarte">
    <div class="brand">
      <span class="brand__dot" aria-hidden="true"></span>
      <div class="brand__text">
        <p class="brand__title">Psychotherapie</p>
        <p class="brand__tagline">für Kinder Jugendliche und Erwachsene</p>
        <p class="brand__name">Dr. med. Monika Haberl</p>
      </div>
    </div>
  </section>

</body>
</html>
```